Bellfield HVAC Business Card design

Looking for a modern professional two sided design. Showing contact info and services provided. Possibly on a silk card stock.
Using blues or greens or greys and maybe metallic. One color or a mixture of these.
Dwayne Ortiz
dortiz@bellfieldhvac-example.net
603-871-4032
Air Conditioning
Heating
Heat Pumps / Gas / Oil
Ductless mini splits
Controls
VFD's
Pumps
Gas Fitting/Piping
Service and New install
Residential / Commercial
Industry/Entity Type
Mechanical HVAC
Contact Information for Business Card
Logo, contact info and provided services
Look and feel

```html
<!DOCTYPE html>
<html lang="en">
<head>
<meta charset="utf-8">
<title>Bellfield HVAC Business Card</title>
<link href="https://fonts.googleapis.com/css2?family=Oswald:wght@500;600&family=Montserrat:wght@400;500;800&display=swap" rel="stylesheet">
<style>
  :root {
    --backdrop-top: #4a4a4c;
    --backdrop-bottom: #2c2c2e;
    --card: #161617;
    --card-edge: #1f6fd1;
    --brand-blue: #1f72c8;
    --ink-white: #f4f4f4;
    --texture-light: #1e1e20;
    --texture-dark: #141415;
  }
  * { box-sizing: border-box; margin: 0; padding: 0; }
  html, body { width: 1200px; height: 1200px; overflow: hidden; }
  body {
    background: linear-gradient(180deg, var(--backdrop-top), var(--backdrop-bottom));
    position: relative;
    font-family: "Montserrat", Arial, sans-serif;
  }
  .card {
    position: absolute;
    left: 250px;
    width: 700px;
    height: 400px;
    background: var(--card);
    border-radius: 36px;
    border-bottom: 3px solid var(--card-edge);
    border-left: 2px solid var(--card-edge);
    box-shadow: 0 18px 40px rgba(0,0,0,.45);
    overflow: hidden;
  }
  .card-front { top: 150px; }
  .card-back { top: 640px; }

  .services {
    position: absolute;
    left: 42px;
    top: 40px;
    list-style: none;
    font-family: "Oswald", "Arial Narrow", sans-serif;
    font-weight: 600;
    font-size: 17px;
    line-height: 20px;
    letter-spacing: .5px;
    color: var(--ink-white);
    text-transform: uppercase;
  }
  .services li::before {
    content: "";
    display: inline-block;
    width: 5px; height: 5px;
    border-radius: 50%;
    background: var(--brand-blue);
    margin: 0 8px 3px 0;
    vertical-align: middle;
  }
  .sector {
    position: absolute;
    left: 55px;
    top: 228px;
    font-family: "Oswald", "Arial Narrow", sans-serif;
    font-weight: 500;
    font-size: 19px;
    letter-spacing: .6px;
    color: var(--brand-blue);
    text-transform: uppercase;
  }
  .divider {
    position: absolute;
    left: 0;
    top: 262px;
    width: 330px;
    height: 2px;
    background: var(--brand-blue);
  }
  .person-name {
    position: absolute;
    left: 55px;
    top: 276px;
    font-weight: 800;
    font-size: 27px;
    letter-spacing: 2px;
    color: var(--brand-blue);
    text-transform: uppercase;
  }
  .person-role {
    position: absolute;
    left: 58px;
    top: 310px;
    font-weight: 400;
    font-size: 17px;
    letter-spacing: 1px;
    color: var(--ink-white);
  }
  .contact {
    position: absolute;
    left: 58px;
    display: flex;
    align-items: center;
    gap: 10px;
    color: var(--ink-white);
    font-weight: 500;
  }
  .contact-phone { top: 338px; font-size: 20px; }
  .contact-email { top: 366px; font-size: 17px; }
  .contact svg { width: 20px; height: 20px; fill: var(--brand-blue); flex: none; }

  .brand-lockup {
    position: absolute;
    right: 40px;
    top: 150px;
    display: flex;
    align-items: center;
    gap: 14px;
  }
  .brand-dot {
    width: 44px; height: 44px;
    border-radius: 50%;
    background: var(--brand-blue);
  }
  .brand-name {
    font-weight: 800;
    font-size: 30px;
    letter-spacing: 1px;
    color: var(--brand-blue);
    text-transform: uppercase;
    line-height: 1.05;
  }

  .back-texture {
    position: absolute;
    inset: 0;
    background: radial-gradient(ellipse at 50% 50%, var(--texture-light), var(--texture-dark) 75%);
  }
  .back-brand {
    position: absolute;
    left: 50%;
    top: 50%;
    transform: translate(-50%, -50%);
    font-weight: 800;
    font-size: 30px;
    letter-spacing: 1px;
    color: var(--brand-blue);
    text-transform: uppercase;
    text-align: center;
    line-height: 1.05;
  }
</style>
</head>
<body>

<section class="card card-front">
  <ul class="services">
    <li>Air Conditioning</li>
    <li>Heating</li>
    <li>Heat Pumps / Gas / Oil</li>
    <li>Ductless Mini Splits</li>
    <li>Controls</li>
    <li>VFD's</li>
    <li>Pumps</li>
    <li>Gas Fitting/Piping</li>
    <li>Service and New Install</li>
  </ul>
  <p class="sector">Residential / Commercial</p>
  <div class="divider"></div>
  <h1 class="person-name">Dwayne Ortiz</h1>
  <p class="person-role">OWNER</p>
  <p class="contact contact-phone">
    <svg viewBox="0 0 24 24" aria-hidden="true"><path d="M6.6 10.8a15.1 15.1 0 0 0 6.6 6.6l2.2-2.2a1 1 0 0 1 1-.25 11.4 11.4 0 0 0 3.6.57 1 1 0 0 1 1 1V20a1 1 0 0 1-1 1A17 17 0 0 1 3 4a1 1 0 0 1 1-1h3.5a1 1 0 0 1 1 1c0 1.25.2 2.45.57 3.57a1 1 0 0 1-.25 1z"/></svg>
    603-871-4032
  </p>
  <p class="contact contact-email">
    <svg viewBox="0 0 24 24" aria-hidden="true"><path d="M2 5h20v14H2z M4 7v.4l8 5.6 8-5.6V7z" fill-rule="evenodd"/></svg>
    dortiz@bellfieldhvac-example.net
  </p>
  <div class="brand-lockup">
    <span class="brand-dot"></span>
    <span class="brand-name">Bellfield<br>HVAC</span>
  </div>
</section>

<section class="card card-back">
  <div class="back-texture" role="img" aria-label="Subtle embossed decorative pattern across the card back"></div>
  <p class="back-brand">Bellfield<br>HVAC</p>
</section>

</body>
</html>
```